Uitnodiging van het huwelijk
doelgroep
Uitnodiging voor onze bruiloft voor vrienden en familie
Conceptuele formulering
Wij willen hutten individuele uitnodigingskaart. Het moet iets bijzonders zijn, dwz straalt iets bijzonders, maar anders vrij eenvoudig en modern en niet cheesy! Op de voorkant van onze huwelijksdatum en onze namen moeten eventueel een foto van ons. misschien zelfs een citaat: "Het geluk is het enige dat verdubbelt als je het (Gustav Mellinger) Uitnodiging voor onze kerk bruiloft misschien een motief, wat doe je het citaat past delen ....

```html
<!DOCTYPE html>
<html lang="de">
<head>
<meta charset="utf-8">
<title>Hochzeitseinladung Carla &amp; Bernd</title>
<link rel="stylesheet" href="https://fonts.googleapis.com/css2?family=Cutive&family=Herr+Von+Muellerhoff&display=swap">
<style>
  :root {
    --paper: #ffffff;
    --cream: #fef0cc;
    --bar: #5c463d;
    --heart: #c0392b;
    --script-red: #b63a2a;
    --script-brown: #8a6a58;
    --body: #8a7468;
    --title: #4a3a30;
  }
  html, body { margin: 0; padding: 0; overflow: hidden; background: var(--paper); }
  .sheet { display: block; width: 1200px; height: 848px; }
  .band { fill: var(--cream); }
  .field { fill: var(--paper); }
  .bar { fill: var(--bar); }
  .heart { fill: var(--heart); font-family: Arial, sans-serif; text-anchor: middle; }
  .small { font-family: 'Cutive', serif; font-size: 4.6px; fill: var(--body); text-anchor: middle; }
  .body-text { font-family: 'Cutive', serif; font-size: 6.2px; fill: var(--body); text-anchor: middle; }
  .title { font-family: 'Cutive', serif; font-size: 15px; fill: var(--title); text-anchor: middle; }
  .script { font-family: 'Herr Von Muellerhoff', cursive; text-anchor: middle; }
  .script-brown { fill: var(--script-brown); font-size: 15px; }
  .script-red { fill: var(--script-red); font-size: 17px; }
  .photo-label { font-family: 'Cutive', serif; font-size: 7px; fill: var(--body); text-anchor: middle; }
</style>
</head>
<body>
<svg class="sheet" viewBox="0 0 1200 848" xmlns="http://www.w3.org/2000/svg">

  <!-- Front cover -->
  <g class="cover">
    <rect class="field" x="68" y="33" width="232" height="232"/>
    <rect class="band" x="68" y="33" width="232" height="77"/>
    <rect class="band" x="68" y="234" width="232" height="31"/>
    <rect class="bar" x="68" y="33" width="4" height="232"/>
    <rect class="bar" x="296" y="33" width="4" height="232"/>
    <text class="title" x="184" y="73">Carla <tspan class="heart" fill="#c0392b">♥</tspan> Bernd</text>
    <text class="script script-brown" x="184" y="90">Was für eine wunderbare Zeit . . .</text>
    <text class="photo-label" x="184" y="164" role="img" aria-label="Platz für ein Foto des Brautpaares">FOTO</text>
    <text class="script script-brown" x="184" y="229">. . . wir heiraten!</text>
  </g>

  <!-- Inner spread, first fold -->
  <g class="spread-top">
    <polygon class="field" points="426,28 655,40 655,273 426,284"/>
    <polygon class="band" points="426,28 655,40 655,117 426,113"/>
    <polygon class="band" points="426,250 655,242 655,273 426,284"/>
    <rect class="field" x="662" y="40" width="225" height="233"/>
    <rect class="band" x="662" y="40" width="225" height="77"/>
    <rect class="band" x="662" y="242" width="225" height="31"/>
    <polygon class="bar" points="426,28 431,28 431,284 426,284"/>
    <rect class="bar" x="654" y="40" width="8" height="233"/>
    <rect class="bar" x="887" y="40" width="5" height="233"/>

    <text class="heart" x="547" y="93" font-size="13">♥</text>
    <g class="rsvp">
      <text class="small" x="547" y="146">Um uns die Planung zu erleichtern, bitten wir um</text>
      <text class="small" x="547" y="153">Deine/Eure Antwort bis spätestens 26. April 2013.</text>
      <text class="small" x="547" y="162">Carla &amp; Bernd Halder, Lindenhofstraße 14, 63799 Waldbrunnen</text>
      <text class="small" x="547" y="170">Telefon: 06021.555301, Email: c.halder@mail.example</text>
      <text class="small" x="547" y="179">Solltet Ihr unseren besonderen Tag mit netten</text>
      <text class="small" x="547" y="186">Überraschungen mitgestalten wollen, so wendet Euch bitte</text>
      <text class="small" x="547" y="193">rechtzeitig an: Sabine Moritz, Telefon: 0170.5550199</text>
      <text class="small" x="547" y="203">Für Zimmerbuchungen:</text>
      <text class="small" x="547" y="210">Hotel am Weiher, Uferweg 3, 63811 Weiherstadt,</text>
      <text class="small" x="547" y="217">www.hotel-am-weiher.example</text>
    </g>

    <text class="heart" x="775" y="96" font-size="13">♥</text>
    <g class="quote">
      <text class="script script-red" x="775" y="165">Das Glück ist das Einzige,</text>
      <text class="script script-red" x="775" y="177">das sich verdoppelt,</text>
      <text class="script script-red" x="775" y="190">wenn man es teilt.</text>
      <text class="small" x="775" y="200">(Gustav Mellinger)</text>
    </g>
  </g>

  <!-- Inner spread, fully opened -->
  <g class="spread-open">
    <polygon class="field" points="426,305 655,316 655,550 426,561"/>
    <polygon class="band" points="426,305 655,316 655,394 426,390"/>
    <polygon class="band" points="426,526 655,518 655,550 426,561"/>
    <rect class="field" x="662" y="316" width="225" height="234"/>
    <rect class="band" x="662" y="316" width="225" height="78"/>
    <rect class="band" x="662" y="518" width="225" height="32"/>
    <polygon class="field" points="895,316 1120,305 1120,561 895,550"/>
    <polygon class="band" points="895,316 1120,305 1120,390 895,394"/>
    <polygon class="band" points="895,518 1120,526 1120,561 895,550"/>
    <rect class="bar" x="426" y="305" width="5" height="256"/>
    <rect class="bar" x="654" y="316" width="8" height="234"/>
    <rect class="bar" x="887" y="316" width="8" height="234"/>
    <rect class="bar" x="1120" y="305" width="4" height="256"/>

    <text class="heart" x="547" y="370" font-size="13">♥</text>
    <g class="rsvp">
      <text class="small" x="547" y="423">Um uns die Planung zu erleichtern, bitten wir um</text>
      <text class="small" x="547" y="430">Deine/Eure Antwort bis spätestens 26. April 2013.</text>
      <text class="small" x="547" y="439">Carla &amp; Bernd Halder, Lindenhofstraße 14, 63799 Waldbrunnen</text>
      <text class="small" x="547" y="447">Telefon: 06021.555301, Email: c.halder@mail.example</text>
      <text class="small" x="547" y="456">Solltet Ihr unseren besonderen Tag mit netten</text>
      <text class="small" x="547" y="463">Überraschungen mitgestalten wollen, so wendet Euch bitte</text>
      <text class="small" x="547" y="470">rechtzeitig an: Sabine Moritz, Telefon: 0170.5550199</text>
      <text class="small" x="547" y="480">Für Zimmerbuchungen:</text>
      <text class="small" x="547" y="487">Hotel am Weiher, Uferweg 3, 63811 Weiherstadt,</text>
      <text class="small" x="547" y="494">www.hotel-am-weiher.example</text>
    </g>

    <text class="script script-red" x="775" y="373" font-size="20">Am 20. Juli 2013</text>
    <g class="invitation">
      <text class="body-text" x="775" y="417">An Silvester wagten wir vor dem Standesamt bereits</text>
      <text class="body-text" x="775" y="425">den ersten Schritt und sagten „Ja“,</text>
      <text class="body-text" x="775" y="433">nun auch den Zweiten, vor den Traualtar!</text>
      <text class="body-text" x="775" y="444">Diesen besonderen Tag möchten wir gemeinsam</text>
      <text class="body-text" x="775" y="451">mit Dir/Euch verbringen.</text>
      <text class="body-text" x="775" y="462">Die Hochzeitsglocken der katholischen Kirche St. Albanus,</text>
      <text class="body-text" x="775" y="469">in Waldbrunnen, läuten für uns um 14:00 Uhr.</text>
      <text class="body-text" x="775" y="480">Anschließend feiern wir im Hotel am Weiher, in Weiherstadt.</text>
      <text class="body-text" x="775" y="490">Wir freuen uns auf Dich/Euch und</text>
      <text class="body-text" x="775" y="498">einen unvergesslichen Tag!</text>
    </g>

    <text class="heart" x="1002" y="370" font-size="13">♥</text>
    <g class="gift-note">
      <text class="small" x="1002" y="431">Liebe Gäste lasst Euch sagen,</text>
      <text class="small" x="1002" y="438">Pakete braucht Ihr nicht zu tragen.</text>
      <text class="small" x="1002" y="447">Auch braucht Ihr nicht zu laufen,</text>
      <text class="small" x="1002" y="455">um Geschenke einzukaufen.</text>
      <text class="small" x="1002" y="464">Denn unser Haushalt der ist voll,</text>
      <text class="small" x="1002" y="471">drum fänden wir es richtig toll,</text>
      <text class="small" x="1002" y="479">ein Kuvert mit etwas drin,</text>
      <text class="small" x="1002" y="486">macht uns Freude und hat Sinn.</text>
    </g>
  </g>

  <!-- Back cover -->
  <g class="back">
    <rect class="band" x="426" y="590" width="233" height="233"/>
    <rect class="bar" x="426" y="590" width="5" height="233"/>
    <rect class="bar" x="654" y="590" width="5" height="233"/>
    <text class="heart" x="542" y="686" font-size="13">♥</text>
    <g class="lyrics">
      <text class="body-text" x="542" y="696">Ja zu jedem Tag mit Dir.</text>
      <text class="body-text" x="542" y="704">Ja zu jedem Deiner Fehler.</text>
      <text class="body-text" x="542" y="712">Asche und Gold, ich trag' alles mit Dir.</text>
      <text class="body-text" x="542" y="720">Denn ich bin und bleib verlor'n in Deiner Mitte.</text>
      <text class="body-text" x="542" y="728">In Deiner Mitte, bis der Vorhang fällt!</text>
      <text class="small" x="542" y="737">(„Ja“ von Nachtfalter)</text>
    </g>
  </g>
</svg>
</body>
</html>
```